Looking for a PowerPoint design for a Pharmaceutical Company

We need a PowerPoint template design to be used company-wide. We are a pharmaceutical company with 63 years of history and want to use a new template design to work more efficiently and effectively. Below are some of the things we are looking for in the new template design.

- Simple, modern, and professional

- Practical for every day use (easy to read, easy to create)

- Slides will be mainly projected or viewed on screens, but should also work fine when printed. (e.g. We do not want to use up our inks / toners printing several pages..)

- It would be great if you could provide us a list of colors that can be effectively used in the slides. (e.g. for highlighting fonts / multiple graph colors / etc.)

- Just as an FYI, our current logo image is (dark) blue. I am not uploading the logo image here because we do not want you to be limited by the current logo image. Depending on the design, we may / may not put our logo image on the slides.

Please feel free to reach out to me if you have any questions. I look forward to seeing your design. Thank you!

Target Market(s)

Pharmaceutical industry. (To be used internally and externally)

Industry/Entity Type

Pharmaceutical

Font styles to use
Sans Serif

Requirements
Must have
• Title slide, Subtitle slide, graphs, charts, tables, bullet points, and any other slide style components normally included.
Nice to have
• - As we are in the pharma industry, we want the slides to give credibility. But we do not want it look "old", "boring", or "typical". Feel free to use unique / fresh colors.
Should not have
• - TOO many colors
• - Please do not use the images on our website, which contain faces. (Any image with faces in it...) They are stock images we bought for the website, and we do not want the images on our slides. (e.g. image of running woman on the main page, image of a surgeon, image of kids playing soccer, etc.)
• - We are not looking for a design that is a modified version of our website design. We are looking for something new.

```html
<!DOCTYPE html>
<html lang="en">
<head>
<meta charset="utf-8">
<title>Pharmaceutical Slide Template</title>
<link href="https://fonts.googleapis.com/css2?family=Lato:wght@300;400;700;900&display=swap" rel="stylesheet">
<style>
:root{--blue:#2b7bbf;--navy:#1d5c96;--sky:#45aee3;--pale:#dcebf6;--ink:#4a4f55;--grey:#8a9098;--bg:#cfd1d3}
*{box-sizing:border-box}
body{margin:0;width:888px;height:1200px;overflow:hidden;background:var(--bg);font-family:'Lato',sans-serif;color:var(--ink)}
.sheet{display:grid;grid-template-columns:repeat(3,281px);grid-auto-rows:159px;gap:8px 9px;padding:16px 13px}
.slide{position:relative;background:#fff;overflow:hidden}
.head{position:absolute;left:10px;top:8px}
.title{font-size:7.2px;color:var(--blue);letter-spacing:.2px;text-transform:uppercase;margin:0;font-weight:400}
.sub{font-size:3.4px;color:var(--grey);margin:1px 0 0}
.brand{position:absolute;right:8px;top:9px;font-size:4px;font-weight:400;color:var(--navy);display:flex;align-items:center;gap:2px;letter-spacing:.2px}
.brand i{width:3.5px;height:3.5px;background:var(--navy);display:block}
.brand-lg{position:absolute;display:flex;align-items:center;justify-content:center;gap:3px;font-weight:400;color:var(--navy);letter-spacing:.3px}
.brand-lg i{background:var(--navy);display:block}
.foot{position:absolute;left:0;right:0;bottom:0;height:8px;background:var(--blue);color:#fff;font-size:3.2px;display:flex;align-items:center;justify-content:space-between;padding:0 6px}
.foot b{font-weight:400;margin-left:5px}
.txt{font-size:3.5px;line-height:1.5;color:var(--grey);margin:0}
.ph{position:absolute}
.c{text-align:center}
.lbl{font-size:4.2px;color:var(--blue);margin:0 0 2px}
svg.ic{display:block;width:100%;height:100%}
.badge{flex:none;display:block;border-radius:50%}
.photo-city{background:linear-gradient(180deg,#e9eef2 0%,#b9c3cb 55%,#7f8c96 100%)}
.photo-lab{background:linear-gradient(135deg,#e8eef3,#b9cbd9 60%,#8ea7bd)}
.photo-blue{background:linear-gradient(135deg,#2f6fa3,#5e9ccb 50%,#1d5c96)}
.num{flex:none;width:13px;height:13px;border-radius:50%;background:var(--blue);color:#fff;font-size:5px;font-weight:700;display:flex;align-items:center;justify-content:center}
.step{flex:none;width:8px;height:8px;border-radius:50%;background:var(--pale);color:var(--blue);font-size:3.2px;display:flex;align-items:center;justify-content:center}
.tag{position:absolute;left:0;right:0;bottom:0;height:9px;background:var(--sky);color:#fff;font-size:4px;display:flex;align-items:center;justify-content:center}
.contact-row{display:flex;align-items:center;gap:6px;font-size:4.5px}
.contact-row .badge{width:13px;height:13px;border:1px solid var(--blue);padding:2px}
</style>
</head>
<body>
<svg width="0" height="0" style="position:absolute" aria-hidden="true">
 <symbol id="i-doc" viewBox="0 0 24 24"><rect x="6" y="4" width="12" height="16" rx="1" fill="none" stroke="#fff" stroke-width="1.6"/><path d="M9 9h6M9 12h6M9 15h4" stroke="#fff" stroke-width="1.6"/></symbol>
 <symbol id="i-bars" viewBox="0 0 24 24"><path d="M6 19V13M10 19V10M14 19V12M18 19V7" stroke="#fff" stroke-width="2.2"/><circle cx="17" cy="5" r="2" fill="#fff"/></symbol>
 <symbol id="i-case" viewBox="0 0 24 24"><rect x="4" y="8" width="16" height="11" rx="1" fill="#fff"/><path d="M9 8V6h6v2" fill="none" stroke="#fff" stroke-width="1.6"/><path d="M4 12h16" stroke="#2b7bbf" stroke-width="1"/></symbol>
 <symbol id="i-watch" viewBox="0 0 24 24"><circle cx="12" cy="13" r="7" fill="none" stroke="#fff" stroke-width="1.8"/><path d="M12 13l3-3M10 4h4" stroke="#fff" stroke-width="1.8"/></symbol>
 <symbol id="i-bulb" viewBox="0 0 24 24"><circle cx="12" cy="10" r="5" fill="none" stroke="#fff" stroke-width="1.8"/><path d="M10 17h4M10 19h4" stroke="#fff" stroke-width="1.6"/></symbol>
 <symbol id="i-pin" viewBox="0 0 24 24"><path d="M12 3a6 6 0 0 1 6 6c0 5-6 12-6 12S6 14 6 9a6 6 0 0 1 6-6z" fill="#2b7bbf"/><circle cx="12" cy="9" r="2" fill="#fff"/></symbol>
 <symbol id="i-phone" viewBox="0 0 24 24"><rect x="7" y="3" width="10" height="18" rx="2" fill="#2b7bbf"/><rect x="9" y="6" width="6" height="10" fill="#fff"/></symbol>
 <symbol id="i-mail" viewBox="0 0 24 24"><rect x="4" y="6" width="16" height="12" rx="1" fill="#2b7bbf"/><path d="M4 7l8 6 8-6" fill="none" stroke="#fff" stroke-width="1.4"/></symbol>
 <symbol id="i-globe" viewBox="0 0 24 24"><circle cx="12" cy="12" r="8" fill="none" stroke="#2b7bbf" stroke-width="1.8"/><path d="M4 12h16M12 4c-4 5-4 11 0 16M12 4c4 5 4 11 0 16" fill="none" stroke="#2b7bbf" stroke-width="1.4"/></symbol>
</svg>

<main class="sheet">

<section class="slide">
 <div class="ph photo-city" style="left:0;top:0;width:281px;height:105px" role="img" aria-label="Hazy city skyline photograph"></div>
 <div class="brand-lg" style="left:94px;top:42px;width:93px;height:16px;background:#fff;font-size:7px"><i style="width:5px;height:5px"></i>Solvane Health</div>
 <div style="position:absolute;left:0;right:0;top:106px;height:1px;background:var(--blue)"></div>
 <p class="c" style="position:absolute;left:0;right:0;top:118px;margin:0;font-size:13px;color:var(--blue)">PRESENTATION TITLE</p>
 <p class="c sub" style="position:absolute;left:0;right:0;top:136px;font-size:4px">Subtitle of presentation here</p>
</section>

<section class="slide">
 <div class="ph" style="inset:0;background:linear-gradient(180deg,#f1f3f5,#d9dfe4 60%,#c3ccd3)" role="img" aria-label="Faded city skyline photograph"></div>
 <div class="brand-lg" style="left:0;right:0;top:54px;font-size:9px"><i style="width:6px;height:6px"></i>Solvane Health</div>
 <p class="c" style="position:absolute;left:0;right:0;top:80px;margin:0;font-size:13px;color:var(--blue)">PRESENTATION TITLE</p>
 <p class="c sub" style="position:absolute;left:0;right:0;top:98px;font-size:4px">Subtitle of presentation here</p>
</section>

<section class="slide">
 <div class="head"><p class="title">Table of Content</p><p class="sub">Subtitle of this slide goes here</p></div>
 <div class="brand"><i></i>Solvane Health</div>
 <div style="position:absolute;left:12px;top:32px;width:260px;display:grid;grid-template-columns:1fr 1fr;gap:10px 14px">
  <div style="display:flex;gap:5px"><span class="num">01</span><div><p class="lbl">Chapter 1</p><p class="txt">Lorem ipsum dolor sit amet, consectetuer adipiscing elit. Aenean commodo ligula eget dolor.</p></div></div>
  <div style="display:flex;gap:5px"><span class="num">04</span><div><p class="lbl">Chapter 4</p><p class="txt">Lorem ipsum dolor sit amet, consectetuer adipiscing elit. Aenean commodo ligula eget dolor.</p></div></div>
  <div style="display:flex;gap:5px"><span class="num">02</span><div><p class="lbl">Chapter 2</p><p class="txt">Lorem ipsum dolor sit amet, consectetuer adipiscing elit. Aenean commodo ligula eget dolor.</p></div></div>
  <div style="display:flex;gap:5px"><span class="num">05</span><div><p class="lbl">Chapter 5</p><p class="txt">Lorem ipsum dolor sit amet, consectetuer adipiscing elit. Aenean commodo ligula eget dolor.</p></div></div>
  <div style="display:flex;gap:5px"><span class="num">03</span><div><p class="lbl">Chapter 3</p><p class="txt">Lorem ipsum dolor sit amet, consectetuer adipiscing elit. Aenean commodo ligula eget dolor.</p></div></div>
  <div style="display:flex;gap:5px"><span class="num">06</span><div><p class="lbl">Chapter 6</p><p class="txt">Lorem ipsum dolor sit amet, consectetuer adipiscing elit. Aenean commodo ligula eget dolor.</p></div></div>
 </div>
 <div class="foot"><span>Copyright © 2016 Solvane. All rights reserved.</span><span>www.solvanehealth.com<b>2</b></span></div>
</section>

<section class="slide">
 <div class="ph" style="left:0;top:0;width:281px;height:58px;background:linear-gradient(180deg,#d9d2c4,#9a9184 60%,#5d5a56)" role="img" aria-label="City skyline at sunset photograph"></div>
 <div class="brand-lg" style="left:0;right:0;top:64px;font-size:4px"><i style="width:3.5px;height:3.5px"></i>Solvane Health</div>
 <p class="c" style="position:absolute;left:0;right:0;top:73px;margin:0;font-size:7px;color:var(--blue)">ABOUT COMPANY</p>
 <div class="c" style="position:absolute;left:14px;right:14px;top:86px"><p class="txt">Lorem ipsum dolor sit amet, consectetuer adipiscing elit. Aenean commodo ligula eget dolor. Aenean massa. Cum sociis natoque penatibus et magnis dis parturient montes.</p><p class="txt" style="margin-top:4px">Aliquam lorem ante, dapibus in, viverra quis, feugiat a, tellus. Phasellus viverra nulla ut metus varius laoreet. Quisque rutrum. Aenean imperdiet. Etiam ultricies nisi vel augue. Curabitur ullamcorper ultricies nisi. Nam eget dui. Etiam rhoncus.</p></div>
 <div class="foot"><span>Copyright © 2016 Solvane. All rights reserved.</span><span>www.solvanehealth.com<b>3</b></span></div>
</section>

<section class="slide">
 <div class="ph" style="left:0;top:0;width:126px;height:151px;background:linear-gradient(160deg,#eef3f7,#b7cfe2 70%,#8fb1cc)" role="img" aria-label="Medical professional in blue scrubs photograph"></div>
 <div class="brand"><i></i>Solvane Health</div>
 <div style="position:absolute;left:146px;top:28px;width:124px">
  <p class="title" style="font-size:7px;margin-bottom:5px">Our Mission</p>
  <p class="txt">Lorem ipsum dolor sit amet, consectetuer adipiscing elit. Aenean commodo ligula eget dolor. Aenean massa. Cum sociis natoque penatibus et magnis dis parturient montes.</p>
  <div style="display:flex;gap:4px;margin-top:6px"><span class="step">01</span><p class="txt">Lorem ipsum dolor sit amet, consectetuer adipiscing elit. Aenean commodo ligula eget dolor.</p></div>
  <div style="display:flex;gap:4px;margin-top:6px"><span class="step">02</span><p class="txt">Lorem ipsum dolor sit amet, consectetuer adipiscing elit. Aenean commodo ligula eget dolor.</p></div>
  <div style="display:flex;gap:4px;margin-top:6px"><span class="step">03</span><p class="txt">Lorem ipsum dolor sit amet, consectetuer adipiscing elit. Aenean commodo ligula eget dolor.</p></div>
 </div>
 <div class="foot"><span>Copyright © 2016 Solvane. All rights reserved.</span><span>www.solvanehealth.com<b>5</b></span></div>
</section>

<section class="slide">
 <div class="ph photo-lab" style="left:0;top:0;width:157px;height:151px" role="img" aria-label="Laboratory researchers with microscope photograph"></div>
 <div class="brand"><i></i>Solvane Health</div>
 <div style="position:absolute;left:166px;top:28px;width:106px">
  <p class="title" style="font-size:7px;margin-bottom:5px">Our Vision</p>
  <div style="background:var(--blue);color:#fff;font-size:3.4px;line-height:1.4;padding:3px 4px 3px 14px;position:relative;margin-bottom:5px"><span style="position:absolute;left:3px;top:0;font-size:11px;font-weight:900">“</span>Success or failure in business is caused more by the mental attitude even than by mental capacities.</div>
  <p class="txt">Lorem ipsum dolor sit amet, consectetuer adipiscing elit. Aenean commodo ligula eget dolor. Aenean massa. Cum sociis natoque penatibus et magnis dis parturient montes.</p>
  <p class="txt" style="margin-top:4px">Aliquam lorem ante, dapibus in, viverra quis, feugiat a, tellus. Phasellus viverra nulla ut metus varius laoreet. Quisque rutrum. Aenean imperdiet. Etiam ultricies nisi vel augue. Curabitur ullamcorper ultricies nisi. Nam eget dui. Etiam rhoncus. Maecenas tempus, tellus eget condimentum rhoncus, sem quam semper libero.</p>
 </div>
 <div class="foot"><span>Copyright © 2016 Solvane. All rights reserved.</span><span>www.solvanehealth.com<b>6</b></span></div>
</section>

<section class="slide">
 <div class="head"><p class="title">Our Service</p><p class="sub">Subtitle of this slide goes here</p></div>
 <div class="brand"><i></i>Solvane Health</div>
 <div class="ph photo-blue" style="left:0;top:26px;width:281px;height:82px" role="img" aria-label="Blue-tinted laboratory photograph"></div>
 <div style="position:absolute;left:8px;right:8px;top:32px;display:grid;grid-template-columns:repeat(4,1fr);gap:4px">
  <div class="c" style="border-right:1px solid rgba(255,255,255,.3);padding:0 3px"><svg style="width:16px;height:16px"><use href="#i-doc"/></svg><p style="font-size:4px;color:#fff;margin:3px 0 2px">Description</p><p class="txt" style="color:#e3eef7">Lorem ipsum dolor sit amet, consectetuer adipiscing elit. Aenean commodo ligula eget dolor.</p></div>
  <div class="c" style="border-right:1px solid rgba(255,255,255,.3);padding:0 3px"><svg style="width:16px;height:16px"><use href="#i-bars"/></svg><p style="font-size:4px;color:#fff;margin:3px 0 2px">Description</p><p class="txt" style="color:#e3eef7">Lorem ipsum dolor sit amet, consectetuer adipiscing elit. Aenean commodo ligula eget dolor.</p></div>
  <div class="c" style="border-right:1px solid rgba(255,255,255,.3);padding:0 3px"><svg style="width:16px;height:16px"><use href="#i-case"/></svg><p style="font-size:4px;color:#fff;margin:3px 0 2px">Description</p><p class="txt" style="color:#e3eef7">Lorem ipsum dolor sit amet, consectetuer adipiscing elit. Aenean commodo ligula eget dolor.</p></div>
  <div class="c" style="padding:0 3px"><svg style="width:16px;height:16px"><use href="#i-watch"/></svg><p style="font-size:4px;color:#fff;margin:3px 0 2px">Description</p><p class="txt" style="color:#e3eef7">Lorem ipsum dolor sit amet, consectetuer adipiscing elit. Aenean commodo ligula eget dolor.</p></div>
 </div>
 <p class="txt c" style="position:absolute;left:12px;right:12px;top:114px">Lorem ipsum dolor sit amet, consectetuer adipiscing elit. Aenean commodo ligula eget dolor. Aenean massa. Cum sociis natoque penatibus et magnis dis parturient montes, nascetur ridiculus mus. Donec quam felis, ultricies nec, pellentesque eu, pretium quis, sem.</p>
 <div class="foot"><span>Copyright © 2016 Solvane. All rights reserved.</span><span>www.solvanehealth.com<b>7</b></span></div>
</section>

<section class="slide">
 <div class="head"><p class="title">Why Choose Our Service</p><p class="sub">Subtitle of this slide goes here</p></div>
 <div class="brand"><i></i>Solvane Health</div>
 <div class="ph" style="left:0;top:26px;width:281px;height:58px;background:linear-gradient(90deg,#6b7a84,#a99a8c 50%,#5d4c44)" role="img" aria-label="Researcher handling a sample vial photograph"></div>
 <div style="position:absolute;left:8px;right:8px;top:76px;display:grid;grid-template-columns:repeat(4,1fr);gap:6px">
  <div class="c"><span class="badge" style="margin:0 auto;width:17px;height:17px;background:var(--blue);border:1.5px solid #fff;padding:2px"><svg class="ic"><use href="#i-doc"/></svg></span><p class="lbl" style="margin:2px 0">Best Service</p><p class="txt">Lorem ipsum dolor sit ameter consecte tuer adipiscingelitar</p></div>
  <div class="c"><span class="badge" style="margin:0 auto;width:17px;height:17px;background:var(--blue);border:1.5px solid #fff;padding:2px"><svg class="ic"><use href="#i-bulb"/></svg></span><p class="lbl" style="margin:2px 0">Best Service</p><p class="txt">Lorem ipsum dolor sit ameter consecte tuer adipiscingelitar</p></div>
  <div class="c"><span class="badge" style="margin:0 auto;width:17px;height:17px;background:var(--blue);border:1.5px solid #fff;padding:2px"><svg class="ic"><use href="#i-watch"/></svg></span><p class="lbl" style="margin:2px 0">Best Service</p><p class="txt">Lorem ipsum dolor sit ameter consecte tuer adipiscingelitar</p></div>
  <div class="c"><span class="badge" style="margin:0 auto;width:17px;height:17px;background:var(--blue);border:1.5px solid #fff;padding:2px"><svg class="ic"><use href="#i-bars"/></svg></span><p class="lbl" style="margin:2px 0">Best Service</p><p class="txt">Lorem ipsum dolor sit ameter consecte tuer adipiscingelitar</p></div>
 </div>
 <div class="foot"><span>Copyright © 2016 Solvane. All rights reserved.</span><span>www.solvanehealth.com<b>8</b></span></div>
</section>

<section class="slide">
 <div class="head"><p class="title">Image and Text</p><p class="sub">Subtitle of this slide goes here</p></div>
 <div class="brand"><i></i>Solvane Health</div>
 <div style="position:absolute;left:8px;right:8px;top:30px;display:grid;grid-template-columns:repeat(4,1fr);gap:8px">
  <div class="c"><div class="photo-lab" style="height:63px" role="img" aria-label="Lab sample rack photograph"></div><p class="lbl" style="margin:3px 0 2px">Image Description</p><p class="txt">Lorem ipsum dolor sit amet, consectetuer adipiscing elit. Aenean commodo ligula eget dolor. Aenean massa.</p></div>
  <div class="c"><div class="photo-lab" style="height:63px" role="img" aria-label="Laboratory glassware photograph"></div><p class="lbl" style="margin:3px 0 2px">Image Description</p><p class="txt">Lorem ipsum dolor sit amet, consectetuer adipiscing elit. Aenean commodo ligula eget dolor. Aenean massa.</p></div>
  <div class="c"><div style="height:63px;background:linear-gradient(135deg,#dfe8ee,#c7b9a5 60%,#9aaebf)" role="img" aria-label="Scientist at microscope photograph"></div><p class="lbl" style="margin:3px 0 2px">Image Description</p><p class="txt">Lorem ipsum dolor sit amet, consectetuer adipiscing elit. Aenean commodo ligula eget dolor. Aenean massa.</p></div>
  <div class="c"><div style="height:63px;background:linear-gradient(135deg,#dbe9f3,#8fc1e3 60%,#5b9ccc)" role="img" aria-label="Pipette and test tubes photograph"></div><p class="lbl" style="margin:3px 0 2px">Image Description</p><p class="txt">Lorem ipsum dolor sit amet, consectetuer adipiscing elit. Aenean commodo ligula eget dolor. Aenean massa.</p></div>
 </div>
 <div class="foot"><span>Copyright © 2016 Solvane. All rights reserved.</span><span>www.solvanehealth.com<b>9</b></span></div>
</section>

<section class="slide">
 <div class="head"><p class="title">Image and Text</p><p class="sub">Subtitle of this slide goes here</p></div>
 <div class="brand"><i></i>Solvane Health</div>
 <div style="position:absolute;left:9px;right:9px;top:26px;display:grid;grid-template-columns:repeat(3,1fr);gap:6px 7px">
  <div style="position:relative;height:52px;background:linear-gradient(135deg,#f5f3ee,#f0d88a 60%,#e6b84c)" role="img" aria-label="Yellow capsules and pill bottle photograph"><span class="tag">IMAGE INFORMATIONS</span></div>
  <div style="position:relative;height:52px;background:linear-gradient(135deg,#f4f0ec,#e8c7b5 60%,#d9a48d)" role="img" aria-label="Assorted pills photograph"><span class="tag">IMAGE INFORMATIONS</span></div>
  <div style="position:relative;height:52px;background:linear-gradient(135deg,#f2f5f7,#c9dbe6 60%,#a7c4d8)" role="img" aria-label="Capsules in clear bottles photograph"><span class="tag">IMAGE INFORMATIONS</span></div>
  <div style="position:relative;height:52px;background:linear-gradient(135deg,#f6f6f6,#e7d3c9 60%,#d18f86)" role="img" aria-label="Colourful tablets spilling from bottle photograph"><span class="tag">IMAGE INFORMATIONS</span></div>
  <div style="position:relative;height:52px;background:linear-gradient(135deg,#f3ead9,#e2c38e 60%,#c89a58)" role="img" aria-label="Pills on wooden table photograph"><span class="tag">IMAGE INFORMATIONS</span></div>
  <div style="position:relative;height:52px;background:linear-gradient(135deg,#cfe1ef,#6fa2cf 60%,#3d74a8)" role="img" aria-label="Blue laboratory vials photograph"><span class="tag">IMAGE INFORMATIONS</span></div>
 </div>
 <div class="foot"><span>Copyright © 2016 Solvane. All rights reserved.</span><span>www.solvanehealth.com<b>10</b></span></div>
</section>

<section class="slide">
 <div class="head"><p class="title">Image and Text</p><p class="sub">Subtitle of this slide goes here</p></div>
 <div class="brand"><i></i>Solvane Health</div>
 <div class="ph photo-lab" style="left:10px;top:28px;width:74px;height:98px" role="img" aria-label="Scientist examining samples photograph"></div>
 <div style="position:absolute;left:96px;top:28px;width:176px">
  <p class="lbl">Sample Heading Here</p>
  <p class="txt">Donec pede justo, fringilla vel, aliquet nec, vulputate eget, arcu. In enim justo, rhoncus ut, imperdiet a, venenatis vitae, justo. Nullam dictum felis eu pede mollis pretium. Integer tincidunt. Cras dapibus. Vivamus elementum semper nisi. Aenean vulputate eleifend tellus. Aenean leo ligula, porttitor eu, consequat vitae, eleifend ac, enim.</p>
  <p style="font-size:3.5px;color:var(--blue);margin:3px 0 1px">• Sample Heading Here</p>
  <p class="txt" style="padding-left:4px">Lorem ipsum dolor sit amet, consectetuer adipiscing elit. Aenean commodo ligula eget dolor. Aenean massa. Cum sociis natoque penatibus et magnis.</p>
  <p style="font-size:3.5px;color:var(--blue);margin:3px 0 1px">• Sample Heading Here</p>
  <p class="txt" style="padding-left:4px">Lorem ipsum dolor sit amet, consectetuer adipiscing elit. Aenean commodo ligula eget dolor. Aenean massa. Cum sociis natoque penatibus et magnis.</p>
  <p style="font-size:3.5px;color:var(--blue);margin:3px 0 1px">• Sample Heading Here</p>
  <p class="txt" style="padding-left:4px">Lorem ipsum dolor sit amet, consectetuer adipiscing elit. Aenean commodo ligula eget dolor. Aenean massa. Cum sociis natoque penatibus et magnis.</p>
 </div>
 <div class="foot"><span>Copyright © 2016 Solvane. All rights reserved.</span><span>www.solvanehealth.com<b>11</b></span></div>
</section>

<section class="slide">
 <div class="head"><p class="title">Iconic Features Slide</p><p class="sub">Subtitle of this slide goes here</p></div>
 <div class="brand"><i></i>Solvane Health</div>
 <div style="position:absolute;left:8px;right:8px;top:30px;display:grid;grid-template-columns:repeat(4,1fr);gap:8px">
  <div class="c"><svg width="40" height="44" viewBox="0 0 40 44"><path d="M20 2l17 10v20L20 42 3 32V12z" fill="var(--sky)"/><svg x="10" y="11" width="20" height="20"><use href="#i-doc"/></svg></svg><p class="lbl" style="margin:3px 0 2px">Description</p><p class="txt">Lorem ipsum dolor sit amet, consectetuer adipiscing elit. Aenean commodo ligula eget dolor. Aenean massa.</p></div>
  <div class="c"><svg width="40" height="44" viewBox="0 0 40 44"><path d="M20 2l17 10v20L20 42 3 32V12z" fill="var(--blue)"/><svg x="10" y="11" width="20" height="20"><use href="#i-bars"/></svg></svg><p class="lbl" style="margin:3px 0 2px">Description</p><p class="txt">Lorem ipsum dolor sit amet, consectetuer adipiscing elit. Aenean commodo ligula eget dolor. Aenean massa.</p></div>
  <div class="c"><svg width="40" height="44" viewBox="0 0 40 44"><path d="M20 2l17 10v20L20 42 3 32V12z" fill="var(--blue)"/><svg x="10" y="11" width="20" height="20"><use href="#i-case"/></svg></svg><p class="lbl" style="margin:3px 0 2px">Description</p><p class="txt">Lorem ipsum dolor sit amet, consectetuer adipiscing elit. Aenean commodo ligula eget dolor. Aenean massa.</p></div>
  <div class="c"><svg width="40" height="44" viewBox="0 0 40 44"><path d="M20 2l17 10v20L20 42 3 32V12z" fill="var(--navy)"/><svg x="10" y="11" width="20" height="20"><use href="#i-watch"/></svg></svg><p class="lbl" style="margin:3px 0 2px">Description</p><p class="txt">Lorem ipsum dolor sit amet, consectetuer adipiscing elit. Aenean commodo ligula eget dolor. Aenean massa.</p></div>
 </div>
 <div class="foot"><span>Copyright © 2016 Solvane. All rights reserved.</span><span>www.solvanehealth.com<b>12</b></span></div>
</section>

<section class="slide">
 <div class="head"><p class="title">Four Cycle Process</p><p class="sub">Subtitle of this slide goes here</p></div>
 <div class="brand"><i></i>Solvane Health</div>
 <svg style="position:absolute;left:104px;top:44px" width="76" height="76" viewBox="0 0 76 76">
  <g fill="none" stroke-width="17">
   <circle cx="38" cy="38" r="27" stroke="var(--sky)" pathLength="100" stroke-dasharray="24 76" transform="rotate(-90 38 38)"/>
   <circle cx="38" cy="38" r="27" stroke="var(--blue)" pathLength="100" stroke-dasharray="24 76" stroke-dashoffset="-25" transform="rotate(-90 38 38)"/>
   <circle cx="38" cy="38" r="27" stroke="var(--navy)" pathLength="100" stroke-dasharray="24 76" stroke-dashoffset="-50" transform="rotate(-90 38 38)"/>
   <circle cx="38" cy="38" r="27" stroke="#3a8fcf" pathLength="100" stroke-dasharray="24 76" stroke-dashoffset="-75" transform="rotate(-90 38 38)"/>
  </g>
  <svg x="46" y="16" width="12" height="12"><use href="#i-case"/></svg>
  <svg x="46" y="48" width="12" height="12"><use href="#i-watch"/></svg>
  <svg x="18" y="48" width="12" height="12"><use href="#i-bars"/></svg>
  <svg x="18" y="16" width="12" height="12"><use href="#i-case"/></svg>
 </svg>
 <div class="c" style="position:absolute;left:12px;top:32px;width:88px"><p class="lbl">Phase One</p><p class="txt">Lorem ipsum dolor sit amet, consectetuer adipiscing elit. Aenean commodo ligula eget dolor. Aenean massa.</p></div>
 <div style="position:absolute;left:196px;top:32px;width:80px"><p class="lbl">Phase Two</p><p class="txt">Lorem ipsum dolor sit amet, consectetuer adipiscing elit. Aenean commodo ligula eget dolor. Aenean massa.</p></div>
 <div class="c" style="position:absolute;left:12px;top:110px;width:88px"><p class="lbl">Phase Four</p><p class="txt">Lorem ipsum dolor sit amet, consectetuer adipiscing elit. Aenean commodo ligula eget dolor. Aenean massa.</p></div>
 <div style="position:absolute;left:196px;top:110px;width:80px"><p class="lbl">Phase Three</p><p class="txt">Lorem ipsum dolor sit amet, consectetuer adipiscing elit. Aenean commodo ligula eget dolor. Aenean massa.</p></div>
 <div class="foot"><span>Copyright © 2016 Solvane. All rights reserved.</span><span>www.solvanehealth.com<b>13</b></span></div>
</section>

<section class="slide">
 <div class="head"><p class="title">Donut Chart</p><p class="sub">Subtitle of this slide goes here</p></div>
 <div class="brand"><i></i>Solvane Health</div>
 <div style="position:absolute;left:8px;right:8px;top:28px;display:grid;grid-template-columns:repeat(4,1fr);gap:6px">
  <div class="c"><svg width="52" height="52" viewBox="0 0 52 52"><circle cx="26" cy="26" r="21" fill="none" stroke="var(--pale)" stroke-width="6"/><circle cx="26" cy="26" r="21" fill="none" stroke="var(--navy)" stroke-width="6" pathLength="100" stroke-dasharray="88 100" transform="rotate(-90 26 26)"/><text x="26" y="29.5" text-anchor="middle" font-size="10" fill="var(--ink)" font-family="Lato,sans-serif">88%</text></svg><p class="lbl" style="margin:2px 0 1px">Market Data</p><p class="txt">Lorem ipsum dolor sit amet, consectetuer adipiscing.</p></div>
  <div class="c"><svg width="52" height="52" viewBox="0 0 52 52"><circle cx="26" cy="26" r="21" fill="none" stroke="var(--pale)" stroke-width="6"/><circle cx="26" cy="26" r="21" fill="none" stroke="var(--blue)" stroke-width="6" pathLength="100" stroke-dasharray="77 100" transform="rotate(-90 26 26)"/><text x="26" y="29.5" text-anchor="middle" font-size="10" fill="var(--ink)" font-family="Lato,sans-serif">77%</text></svg><p class="lbl" style="margin:2px 0 1px">Market Data</p><p class="txt">Lorem ipsum dolor sit amet, consectetuer adipiscing.</p></div>
  <div class="c"><svg width="52" height="52" viewBox="0 0 52 52"><circle cx="26" cy="26" r="21" fill="none" stroke="var(--pale)" stroke-width="6"/><circle cx="26" cy="26" r="21" fill="none" stroke="var(--navy)" stroke-width="6" pathLength="100" stroke-dasharray="66 100" transform="rotate(-90 26 26)"/><text x="26" y="29.5" text-anchor="middle" font-size="10" fill="var(--ink)" font-family="Lato,sans-serif">66%</text></svg><p class="lbl" style="margin:2px 0 1px">Market Data</p><p class="txt">Lorem ipsum dolor sit amet, consectetuer adipiscing.</p></div>
  <div class="c"><svg width="52" height="52" viewBox="0 0 52 52"><circle cx="26" cy="26" r="21" fill="none" stroke="var(--pale)" stroke-width="6"/><circle cx="26" cy="26" r="21" fill="none" stroke="var(--blue)" stroke-width="6" pathLength="100" stroke-dasharray="55 100" transform="rotate(-90 26 26)"/><text x="26" y="29.5" text-anchor="middle" font-size="10" fill="var(--ink)" font-family="Lato,sans-serif">55%</text></svg><p class="lbl" style="margin:2px 0 1px">Market Data</p><p class="txt">Lorem ipsum dolor sit amet, consectetuer adipiscing.</p></div>
 </div>
 <p class="txt c" style="position:absolute;left:12px;right:12px;top:120px">Lorem ipsum dolor sit amet, consectetuer adipiscing elit. Aenean commodo ligula eget dolor. Aenean massa. Cum sociis natoque penatibus et magnis dis parturient montes, nascetur ridiculus mus. Donec quam felis, ultricies nec, pellentesque eu, pretium quis, sem. Nulla consequat massa quis enim.</p>
 <div class="foot"><span>Copyright © 2016 Solvane. All rights reserved.</span><span>www.solvanehealth.com<b>14</b></span></div>
</section>

<section class="slide">
 <div class="head"><p class="title">Pie Chart</p><p class="sub">Subtitle of this slide goes here</p></div>
 <div class="brand"><i></i>Solvane Health</div>
 <svg style="position:absolute;left:16px;top:36px" width="96" height="96" viewBox="0 0 96 96" font-family="Lato,sans-serif">
  <g fill="none" stroke-width="20" transform="rotate(-90 48 48)">
   <circle cx="48" cy="48" r="36" stroke="var(--sky)" pathLength="100" stroke-dasharray="55 100"/>
   <circle cx="48" cy="48" r="36" stroke="var(--navy)" pathLength="100" stroke-dasharray="12 100" stroke-dashoffset="-55"/>
   <circle cx="48" cy="48" r="36" stroke="var(--blue)" pathLength="100" stroke-dasharray="20 100" stroke-dashoffset="-67"/>
   <circle cx="48" cy="48" r="36" stroke="#3a8fcf" pathLength="100" stroke-dasharray="13 100" stroke-dashoffset="-87"/>
  </g>
  <g font-size="5" fill="#fff"><text x="80" y="51">55%</text><text x="30" y="16">12%</text><text x="8" y="42">20%</text><text x="13" y="76">13%</text></g>
  <g transform="translate(38 38) scale(.833)"><path d="M6 19V13M10 19V10M14 19V12M18 19V7" stroke="var(--navy)" stroke-width="2.2"/><circle cx="17" cy="5" r="2" fill="var(--navy)"/></g>
 </svg>
 <div style="position:absolute;left:126px;top:48px;width:146px"><p class="lbl" style="font-size:5.5px">Columns Style Chart Slide</p><p class="txt">Lorem ipsum dolor sit amet, consectetuer adipiscing elit. Aenean commodo ligula eget dolor. Aenean massa. Cum sociis natoque penatibus et magnis dis parturient montes.</p><p class="txt" style="margin-top:4px">Aliquam lorem ante, dapibus in, viverra quis, feugiat a, tellus. Phasellus viverra nulla ut metus varius laoreet. Quisque rutrum. Aenean imperdiet. Etiam ultricies nisi vel augue. Curabitur ullamcorper ultricies nisi. Nam eget dui. Etiam rhoncus. Maecenas tempus, tellus eget condimentum rhoncus, sem quam semper libero.</p></div>
 <div class="foot"><span>Copyright © 2016 Solvane. All rights reserved.</span><span>www.solvanehealth.com<b>15</b></span></div>
</section>

<section class="slide">
 <div class="head"><p class="title">Bar Chart Layout</p><p class="sub">Subtitle of this slide goes here</p></div>
 <div class="brand"><i></i>Solvane Health</div>
 <div style="position:absolute;left:8px;top:44px;width:124px"><p class="lbl" style="font-size:5.5px">Columns Style Chart Slide</p><p class="txt">Lorem ipsum dolor sit amet, consectetuer adipiscing elit. Aenean commodo ligula eget dolor. Aenean massa. Cum sociis natoque penatibus et magnis dis parturient montes.</p><p class="txt" style="margin-top:4px">Aliquam lorem ante, dapibus in, viverra quis, feugiat a, tellus. Phasellus viverra nulla ut metus varius laoreet. Quisque rutrum. Aenean imperdiet. Etiam ultricies nisi vel augue. Curabitur ullamcorper ultricies nisi. Nam eget dui.</p></div>
 <svg style="position:absolute;left:148px;top:34px" width="126" height="96" viewBox="0 0 126 96" font-family="Lato,sans-serif">
  <g font-size="3.5" fill="var(--grey)" text-anchor="end"><text x="8" y="6">40</text><text x="8" y="17">35</text><text x="8" y="28">30</text><text x="8" y="39">25</text><text x="8" y="50">20</text><text x="8" y="61">15</text><text x="8" y="72">10</text><text x="8" y="83">5</text></g>
  <line x1="11" y1="86" x2="124" y2="86" stroke="#ccd" stroke-width=".5"/>
  <g fill="var(--sky)"><rect x="16" y="30" width="3" height="56"/><rect x="44" y="18" width="3" height="68"/><rect x="72" y="40" width="3" height="46"/><rect x="100" y="52" width="3" height="34"/></g>
  <g fill="var(--blue)"><rect x="20" y="10" width="3" height="76"/><rect x="48" y="44" width="3" height="42"/><rect x="76" y="8" width="3" height="78"/><rect x="104" y="30" width="3" height="56"/></g>
  <g fill="var(--navy)"><rect x="24" y="24" width="3" height="62"/><rect x="52" y="56" width="3" height="30"/><rect x="80" y="34" width="3" height="52"/><rect x="108" y="60" width="3" height="26"/></g>
  <g fill="#9fd0ee"><rect x="28" y="48" width="3" height="38"/><rect x="56" y="36" width="3" height="50"/><rect x="84" y="60" width="3" height="26"/><rect x="112" y="44" width="3" height="42"/></g>
  <g font-size="3.5" fill="var(--grey)" text-anchor="middle"><text x="24" y="92">January</text><text x="52" y="92">February</text><text x="80" y="92">March</text><text x="108" y="92">April</text></g>
 </svg>
 <div class="foot"><span>Copyright © 2016 Solvane. All rights reserved.</span><span>www.solvanehealth.com<b>16</b></span></div>
</section>

<section class="slide">
 <div class="head"><p class="title">Table Slide</p><p class="sub">Subtitle of this slide goes here</p></div>
 <div class="brand"><i></i>Solvane Health</div>
 <p class="txt c" style="position:absolute;left:12px;right:12px;top:28px">Lorem ipsum dolor sit amet, consectetuer adipiscing elit. Aenean commodo ligula eget dolor. Aenean massa. Cum sociis natoque penatibus et magnis dis parturient montes, nascetur ridiculus mus. Donec quam felis, ultricies nec.</p>
 <table style="position:absolute;left:10px;top:54px;width:261px;border-collapse:collapse;font-size:3.6px;color:var(--ink);text-align:center">
  <thead><tr style="background:var(--blue);color:#fff;height:8px"><th style="font-weight:400;text-align:left;padding-left:4px">Item Description</th><th style="font-weight:400">Number</th><th style="font-weight:400">Number</th><th style="font-weight:400">Text Title</th><th style="font-weight:400">Text Title</th></tr></thead>
  <tbody>
   <tr style="height:10.5px;border-bottom:.5px solid #dde"><td style="text-align:left;padding-left:12px">Lorem Ipsum</td><td>4.3</td><td>4.2</td><td>Important Data Analysis</td><td>Yes</td></tr>
   <tr style="height:10.5px;border-bottom:.5px solid #dde"><td style="text-align:left;padding-left:12px">Lorem Ipsum</td><td>4.1</td><td>4.4</td><td>Important Data Analysis</td><td>No</td></tr>
   <tr style="height:10.5px;border-bottom:.5px solid #dde"><td style="text-align:left;padding-left:12px">Lorem Ipsum</td><td>3.3</td><td>3.5</td><td>Important Data Analysis</td><td>Yes</td></tr>
   <tr style="height:10.5px;border-bottom:.5px solid #dde"><td style="text-align:left;padding-left:12px">Lorem Ipsum</td><td>2.1</td><td>2.8</td><td>Important Data Analysis</td><td>No</td></tr>
   <tr style="height:10.5px;border-bottom:.5px solid #dde"><td style="text-align:left;padding-left:12px">Lorem Ipsum</td><td>1.7</td><td>1.3</td><td>Important Data Analysis</td><td>Yes</td></tr>
   <tr style="height:22px;background:#4a4d52"><td colspan="5"></td></tr>
  </tbody>
 </table>
 <div class="foot"><span>Copyright © 2016 Solvane. All rights reserved.</span><span>www.solvanehealth.com<b>17</b></span></div>
</section>

<section class="slide">
 <div class="head"><p class="title">SWOT Analysis</p><p class="sub">Subtitle of this slide goes here</p></div>
 <div class="brand"><i></i>Solvane Health</div>
 <svg style="position:absolute;left:94px;top:28px" width="94" height="100" viewBox="0 0 94 100" font-family="Lato,sans-serif">
  <circle cx="47" cy="50" r="44" fill="none" stroke="#d8dde2" stroke-width="2"/>
  <circle cx="27" cy="30" r="18" fill="var(--sky)"/><circle cx="67" cy="30" r="18" fill="var(--sky)"/>
  <circle cx="27" cy="70" r="18" fill="var(--navy)"/><circle cx="67" cy="70" r="18" fill="var(--blue)"/>
  <circle cx="47" cy="50" r="14" fill="#8a8f96" stroke="#fff" stroke-width="1.5"/>
  <text x="47" y="53" text-anchor="middle" font-size="7.5" fill="#fff">SWOT</text>
  <g font-size="4" fill="#fff" text-anchor="middle"><text x="24" y="37">Strengths</text><text x="70" y="37">Weakness</text><text x="24" y="83">Opportunity</text><text x="70" y="83">Threats</text></g>
  <svg x="19" y="18" width="12" height="12"><use href="#i-bars"/></svg><svg x="63" y="18" width="12" height="12"><use href="#i-watch"/></svg>
  <svg x="19" y="59" width="12" height="12"><use href="#i-case"/></svg><svg x="63" y="59" width="12" height="12"><use href="#i-bulb"/></svg>
 </svg>
 <p class="txt c" style="position:absolute;left:10px;top:40px;width:78px">Lorem ipsum dolor sit amet, consectetu adipiscing elit. Aenean commodo ligula eget dolor. Aenean massa.</p>
 <p class="txt c" style="position:absolute;left:194px;top:40px;width:78px">Lorem ipsum dolor sit amet, consectetu adipiscing elit. Aenean commodo ligula eget dolor. Aenean massa.</p>
 <p class="txt c" style="position:absolute;left:10px;top:94px;width:78px">Lorem ipsum dolor sit amet, consectetu adipiscing elit. Aenean commodo ligula eget dolor. Aenean massa.</p>
 <p class="txt c" style="position:absolute;left:194px;top:94px;width:78px">Lorem ipsum dolor sit amet, consectetu adipiscing elit. Aenean commodo ligula eget dolor. Aenean massa.</p>
 <div class="foot"><span>Copyright © 2016 Solvane. All rights reserved.</span><span>www.solvanehealth.com<b>18</b></span></div>
</section>

<section class="slide">
 <div class="head"><p class="title">Text Layout</p><p class="sub">Subtitle of this slide goes here</p></div>
 <div class="brand"><i></i>Solvane Health</div>
 <div style="position:absolute;left:10px;top:28px;width:86px"><p class="txt" style="color:var(--blue);text-align:justify">Lorem ipsum dolor sit amet, consectetuer adipiscing elit. Aenean commodo ligula eget dolor. Aenean massa. Cum sociis natoque penatibus et magnis dis parturient montes, nascetur ridiculus mus.</p><p class="txt" style="margin-top:4px;text-align:justify">Donec pede justo, fringilla vel, aliquet nec, vulputate eget, arcu. In enim justo, rhoncus ut, imperdiet a, venenatis vitae, justo. Nullam dictum felis eu pede mollis pretium. Integer tincidunt. Cras dapibus. Vivamus elementum semper nisi. Aenean vulputate eleifend tellus. Aenean leo ligula, porttitor eu, consequat vitae, eleifend ac, enim. Aliquam lorem ante, dapibus in, viverra quis, feugiat a, tellus.</p></div>
 <div style="position:absolute;left:106px;top:28px;width:166px">
  <p class="txt" style="text-align:justify">Lorem ipsum dolor sit amet, consectetuer adipiscing elit. Aenean commodo ligula eget dolor. Aenean massa. Cum sociis natoque penatibus et magnis dis parturient montes, nascetur ridiculus mus. Donec quam felis, ultricies nec, pellentesque eu, pretium quis, sem. Nulla consequat massa quis enim. Donec pede justo, fringilla vel, aliquet nec, vulputate eget, arcu.</p>
  <p style="font-size:4px;color:var(--ink);margin:4px 0 4px">Subtitle of presentation here</p>
  <div style="display:grid;grid-template-columns:1fr 1fr;gap:6px 8px">
   <div style="display:flex;gap:3px"><span class="badge" style="width:11px;height:11px;background:var(--blue);padding:1.5px"><svg class="ic"><use href="#i-doc"/></svg></span><div><p class="lbl" style="font-size:3.8px;margin:0">Description</p><p class="txt">consectetuer adipiscing elit dolor magnis dis parturient montes.</p></div></div>
   <div style="display:flex;gap:3px"><span class="badge" style="width:11px;height:11px;background:var(--blue);padding:1.5px"><svg class="ic"><use href="#i-bulb"/></svg></span><div><p class="lbl" style="font-size:3.8px;margin:0">Description</p><p class="txt">consectetuer adipiscing elit dolor magnis dis parturient montes.</p></div></div>
   <div style="display:flex;gap:3px"><span class="badge" style="width:11px;height:11px;background:var(--blue);padding:1.5px"><svg class="ic"><use href="#i-watch"/></svg></span><div><p class="lbl" style="font-size:3.8px;margin:0">Description</p><p class="txt">consectetuer adipiscing elit dolor magnis dis parturient montes.</p></div></div>
   <div style="display:flex;gap:3px"><span class="badge" style="width:11px;height:11px;background:var(--blue);padding:1.5px"><svg class="ic"><use href="#i-case"/></svg></span><div><p class="lbl" style="font-size:3.8px;margin:0">Description</p><p class="txt">consectetuer adipiscing elit dolor magnis dis parturient montes.</p></div></div>
  </div>
 </div>
 <div class="foot"><span>Copyright © 2016 Solvane. All rights reserved.</span><span>www.solvanehealth.com<b>19</b></span></div>
</section>

<section class="slide">
 <div class="ph" style="inset:0;background:linear-gradient(90deg,#1d4f7e,#3a78ab 40%,#7aa7c9 70%,#bcd3e4)" role="img" aria-label="Blue-tinted laboratory photograph"></div>
 <div style="position:absolute;left:76px;top:50px;width:205px;height:46px;background:rgba(255,255,255,.85)"></div>
 <div class="badge" style="position:absolute;left:82px;top:52px;width:42px;height:42px;background:var(--navy);padding:8px"><svg class="ic"><use href="#i-watch"/></svg></div>
 <p style="position:absolute;left:128px;top:56px;margin:0;font-size:14px;color:var(--blue)">SECTION BREAKS</p>
 <p class="txt" style="position:absolute;left:128px;top:74px;width:140px">Lorem ipsum dolor sit amet, consectetuer adipiscing elit. In tortor in urna pulvinar blandit. Aliquam dolor nulla, vitae cursus dapibus, vel eleifend tellus. Vivamus vitae vestibulum massa.</p>
</section>

<section class="slide">
 <div class="ph" style="left:131px;top:0;width:150px;height:159px;background:linear-gradient(135deg,#e9e3da,#c9b8a4 55%,#8e7f70)" role="img" aria-label="Office worker with headset photograph"></div>
 <div class="brand-lg" style="left:12px;top:20px;justify-content:flex-start;font-size:8px"><i style="width:6px;height:6px"></i>Solvane Health</div>
 <div style="position:absolute;left:14px;top:42px;width:108px;border-bottom:1px solid var(--blue)"><p style="margin:0 0 3px;font-size:10px;color:var(--ink)">CONTACT US</p></div>
 <div style="position:absolute;left:12px;top:60px;display:grid;gap:8px">
  <div class="contact-row"><span class="badge"><svg class="ic"><use href="#i-pin"/></svg></span><span>Address Street</span></div>
  <div class="contact-row"><span class="badge"><svg class="ic"><use href="#i-phone"/></svg></span><span>123 456 789</span></div>
  <div class="contact-row"><span class="badge"><svg class="ic"><use href="#i-mail"/></svg></span><span>info@yourdomain.com</span></div>
  <div class="contact-row"><span class="badge"><svg class="ic"><use href="#i-globe"/></svg></span><span>www.yourwebsite.com</span></div>
 </div>
</section>

</main>
</body>
</html>
```